Online Rug Store needs Clearance Banner

Website is: Lanternfield Carpets and Home
You can access it at: www.lanternfieldcarpetsandhome.com and login (top right) with password: trazok

*** update: When creating banners for my site, you have permission to use images from www.velbora.com, but ONLY for this project. The images/artwork are copyright allowable for use on www.lanternfieldcarpetsandhome.com projects.***

We need a home page banner sized 1000 wide x 500 tall pixels to promote a "Clearance Sale" on rugs. The banner can state:

1. Clearance Sale
2. Now in progress
3. Save an extra 20% with coupon code 'Mint20'
4. Ends March 31st
5. Plus Free Shipping and 30 day returns.

We prefer a banner that appears hand-drawn and artistic, not commercially produced. It is OK to use a room scene image, rug images, or just a colored/textured background with text and no images. Your choice.

Flat graphics with no shadows and 3-D effect preferred.
Attached is are 3 logo options, as well as an example banner with handcrafted, artistic styling that we prefer.

Target Market(s)

This should be an eye-catching banner to showcase a very urgent promotion. Consider using colors of red, white, gold, and black to make a strong statement on the home page.

Industry/Entity Type

Home And Garden

Requirements
Must have
• Winner must provide Photoshop editable file format (.psd format) including layers that can be edited.
Nice to have
• Hand-drawn, stenciled, scribbled, artistic graphics and fonts is nice because we sell rugs that are made by hand.
Should not have
• little to no shadowing. Avoid computerized graphics.

```html
<!DOCTYPE html>
<html lang="en">
<head>
<meta charset="utf-8">
<title>Clearance Sale Banner</title>
<link href="https://fonts.googleapis.com/css2?family=Montserrat:wght@300;400;700&family=Dekko&display=swap" rel="stylesheet">
<style>
  :root {
    --gold: #e2b56d;
    --gold-light: #e9c283;
    --band: #f8f1ea;
    --red: #a3202c;
    --red-badge: #b23a41;
    --white: #ffffff;
    --cream: #fbeee2;
  }
  * { margin: 0; padding: 0; box-sizing: border-box; }
  html, body { width: 1200px; height: 600px; overflow: hidden; background: var(--gold); }
  .banner {
    position: relative;
    width: 1200px;
    height: 600px;
    background: linear-gradient(180deg, var(--gold-light), var(--gold));
    font-family: "Montserrat", sans-serif;
  }
  .rug-row {
    position: absolute;
    top: 62px;
    left: 0;
    width: 1200px;
    height: 300px;
  }
  .rug { position: absolute; top: 0; }
  .sale-band {
    position: absolute;
    left: 0;
    top: 392px;
    width: 1200px;
    height: 92px;
    background: var(--band);
    display: flex;
    align-items: center;
    justify-content: center;
  }
  .sale-title {
    font-size: 66px;
    font-weight: 300;
    letter-spacing: 7px;
    color: var(--red);
    line-height: 1;
  }
  .sale-title strong { font-weight: 700; letter-spacing: 5px; }
  .offer {
    position: absolute;
    top: 506px;
    left: 0;
    width: 1200px;
    text-align: center;
    color: var(--white);
  }
  .offer-coupon { font-size: 19px; font-weight: 400; letter-spacing: 0.6px; }
  .offer-coupon b { font-weight: 700; }
  .offer-perks {
    margin-top: 12px;
    font-size: 19px;
    font-weight: 400;
    letter-spacing: 1.5px;
  }
  .end-badge {
    position: absolute;
    left: 942px;
    top: 422px;
    width: 150px;
    height: 150px;
    border-radius: 50%;
    background: var(--red-badge);
    border: 5px solid var(--white);
    display: flex;
    align-items: center;
    justify-content: center;
    text-align: center;
    font-family: "Dekko", cursive;
    font-size: 25px;
    line-height: 1.2;
    color: var(--white);
  }
</style>
</head>
<body>
  <div class="banner">
    <div class="rug-row">
      <svg class="rug" style="left:36px" width="252" height="252" viewBox="0 0 252 252" role="img" aria-label="Round scalloped rug with black border and red medallion">
        <defs><radialGradient id="rugA"><stop offset="0" stop-color="#9c7a55"/><stop offset="0.45" stop-color="#8e1f24"/><stop offset="0.8" stop-color="#2a1a22"/><stop offset="1" stop-color="#1b1420"/></radialGradient></defs>
        <circle cx="126" cy="126" r="124" fill="url(#rugA)"/>
      </svg>
      <svg class="rug" style="left:330px" width="252" height="252" viewBox="0 0 252 252" role="img" aria-label="Round scalloped rug with ivory field and red border">
        <defs><radialGradient id="rugB"><stop offset="0" stop-color="#efe0cf"/><stop offset="0.7" stop-color="#e6cdb3"/><stop offset="0.88" stop-color="#b2453e"/><stop offset="1" stop-color="#e8cdb1"/></radialGradient></defs>
        <circle cx="126" cy="126" r="124" fill="url(#rugB)"/>
      </svg>
      <svg class="rug" style="left:630px" width="260" height="260" viewBox="0 0 260 260" role="img" aria-label="Flower-shaped rug with black floral field and red border">
        <defs><radialGradient id="rugC"><stop offset="0" stop-color="#1e1a22"/><stop offset="0.72" stop-color="#231c24"/><stop offset="0.85" stop-color="#a92a32"/><stop offset="1" stop-color="#1a1418"/></radialGradient></defs>
        <circle cx="130" cy="126" r="126" fill="url(#rugC)"/>
      </svg>
      <svg class="rug" style="left:920px" width="252" height="252" viewBox="0 0 252 252" role="img" aria-label="Round scalloped rug with rust field and cream border">
        <defs><radialGradient id="rugD"><stop offset="0" stop-color="#b24a36"/><stop offset="0.72" stop-color="#a8412f"/><stop offset="0.86" stop-color="#e6d0a8"/><stop offset="1" stop-color="#a33c2c"/></radialGradient></defs>
        <circle cx="126" cy="126" r="124" fill="url(#rugD)"/>
      </svg>
    </div>

    <div class="sale-band">
      <h1 class="sale-title">CLEARANCE <strong>SALE</strong></h1>
    </div>

    <div class="offer">
      <p class="offer-coupon">Save an extra 20% with coupon code <b>'Mint20'</b></p>
      <p class="offer-perks">FREE SHIPPING &nbsp;|&nbsp; 30 DAY RETURNS</p>
    </div>

    <div class="end-badge">End<br>March<br>31st</div>
  </div>
</body>
</html>
```